New Year's Eve Wedding Save the Date

Lise and Marcus (we) are getting married 2016-12-31. I'm a hockey player, and she's into movies... we have 2 yellow labs, and we want a Save the Date postcard that matches our personality and the excitement of the event. See attached mock up that I've created (which will be what we fall back on if we can't find a design we like). I like the idea of the silhouette people and dogs under fireworks but am open to other concepts as well. String lights, champagne bottles/flutes, etc...

Industry/Entity Type

Wedding

Font styles to use
Script

```html
<!DOCTYPE html>
<html lang="en">
<head>
<meta charset="utf-8">
<title>Save the Date – Marcus &amp; Lise</title>
<link rel="stylesheet" href="https://fonts.googleapis.com/css2?family=Pinyon+Script&family=Playfair+Display:ital@1&display=swap">
<style>
  :root {
    --paper: #fbfaf5;
    --paper-warm: #f3ead6;
    --champagne: #e6cf9f;
    --glitter-gold: #d8c23a;
    --glitter-shadow: #b49a4a;
    --ink: #1f2424;
    --bronze-light: #e2bb7c;
    --bronze-dark: #8e7430;
  }
  html, body {
    margin: 0;
    padding: 0;
    overflow: hidden;
  }
  .postcard {
    position: relative;
    width: 1200px;
    height: 930px;
    overflow: hidden;
    background:
      radial-gradient(circle at 95% 12%, var(--champagne) 0%, rgba(230,207,159,0) 30%),
      radial-gradient(circle at 85% 0%, #e9d3a4 0%, rgba(233,211,164,0) 25%),
      radial-gradient(ellipse at 50% 55%, var(--paper) 0%, var(--paper) 45%, var(--paper-warm) 100%);
  }
  .bokeh {
    position: absolute;
    border-radius: 50%;
    border: 2px solid rgba(255,255,255,0.55);
    background: rgba(255,255,255,0.18);
  }
  .headline {
    position: absolute;
    left: 0;
    top: 150px;
    width: 1200px;
    margin: 0;
    text-align: center;
    font-family: "Pinyon Script", cursive;
    font-weight: 400;
    font-size: 172px;
    line-height: 1;
    letter-spacing: 4px;
    color: var(--glitter-gold);
    text-shadow: 3px 3px 0 var(--glitter-shadow), 5px 6px 6px rgba(120,100,40,0.25);
  }
  .couple, .wedding-date {
    position: absolute;
    left: 0;
    width: 1200px;
    margin: 0;
    text-align: center;
    font-family: "Playfair Display", serif;
    font-style: italic;
    font-weight: 400;
    font-size: 78px;
    line-height: 1;
    color: var(--ink);
  }
  .couple { top: 384px; left: -8px; }
  .wedding-date { top: 482px; left: -8px; }
  .silhouette {
    position: absolute;
    left: 400px;
    top: 598px;
    width: 400px;
    height: 306px;
    border-radius: 8px 8px 2px 2px;
    background: radial-gradient(ellipse at 55% 45%, var(--bronze-light) 0%, #c9a461 45%, var(--bronze-dark) 100%);
    box-shadow: 3px 4px 6px rgba(90,70,30,0.3);
  }
</style>
</head>
<body>
  <main class="postcard">
    <span class="bokeh" style="left:-60px;top:-40px;width:260px;height:260px"></span>
    <span class="bokeh" style="left:300px;top:140px;width:180px;height:180px"></span>
    <span class="bokeh" style="left:940px;top:40px;width:120px;height:120px"></span>
    <span class="bokeh" style="left:1120px;top:60px;width:60px;height:60px"></span>
    <span class="bokeh" style="left:20px;top:360px;width:240px;height:240px"></span>
    <span class="bokeh" style="left:960px;top:340px;width:260px;height:260px"></span>
    <span class="bokeh" style="left:40px;top:820px;width:70px;height:70px"></span>
    <span class="bokeh" style="left:880px;top:620px;width:200px;height:200px"></span>

    <h1 class="headline">Save the Date</h1>
    <p class="couple">Marcus &amp; Lise</p>
    <p class="wedding-date">12.31.2016</p>

    <div class="silhouette" role="img" aria-label="Gold silhouette of the couple kissing with their two dogs beside them"></div>
  </main>
</body>
</html>
```